Modern Business Card Design Needed for Young Realtor

Information that is going on the card:Marvin Pold
Broker/Owner
555.210.3367
Marvin@MPoldRealty.com
www.MPoldRealty.com

Would also like to include my plain square marker Handle somewhere. Probably on the back: the_queencity_realtorMy previous business card is attached, I like that one but would like an updated version and maybe a few design changes

Marvin Pold
Broker/Owner
555.210.3367
Marvin@MPoldRealty.com
www.MPoldRealty.com

• Would also like to include my plain square marker Handle somewhere. Probably on the back: the_pinecrest_realtor
• Dorrance Hale or the DH (logo from the previous card.)

```html
<!DOCTYPE html>
<html lang="en">
<head>
<meta charset="utf-8">
<title>MPold Realty — Business Card</title>
<link href="https://fonts.googleapis.com/css2?family=Source+Sans+3:wght@400;600&display=swap" rel="stylesheet">
<style>
  :root{
    --canvas:#ffffff;
    --trim:#5a7bc4;
    --brand-red:#a81f2f;
    --band-gray:#878787;
    --ring-gray:#8a8a8a;
    --ink:#ffffff;
    --handle-gray:#6f6f6f;
    --mark-dark:#2b2b2b;
  }
  *{margin:0;padding:0;box-sizing:border-box}
  html,body{width:1000px;height:1200px;overflow:hidden;background:var(--canvas)}
  body{position:relative;font-family:"Source Sans 3",Arial,sans-serif}
  .card{position:absolute;left:165px;width:664px;height:430px;border:1px solid var(--trim);background:#fff;overflow:hidden}
  .card--front{top:114px}
  .card--back{top:655px}
  .card__art{position:absolute;inset:0}
  .wordmark{position:absolute;color:var(--brand-red);font-weight:400;letter-spacing:.16em;white-space:nowrap;line-height:1}
  .card--front .wordmark{left:42px;top:74px;font-size:31px}
  .card--back .wordmark{left:0;right:0;top:190px;text-align:center;font-size:60px}
  .identity{position:absolute;left:31px;top:197px;color:var(--ink)}
  .identity__name{font-size:27px;font-weight:400;line-height:1.1}
  .identity__role{font-size:13.5px;line-height:1.2}
  .contacts{position:absolute;left:32px;top:308px;list-style:none;color:var(--ink);font-size:14.5px}
  .contacts li{display:flex;align-items:center;height:32px}
  .contacts svg{width:16px;height:16px;margin-right:10px;flex:none}
  .social{position:absolute;left:140px;bottom:10px;display:flex;align-items:center;color:var(--handle-gray);font-size:19px;letter-spacing:.5em}
  .social__marker{width:25px;height:25px;border:3px solid var(--mark-dark);border-radius:5px;margin-right:10px}
</style>
</head>
<body>

<section class="card card--front">
  <svg class="card__art" viewBox="0 0 664 430" width="664" height="430">
    <circle cx="515" cy="181" r="148" fill="var(--ring-gray)"/>
    <circle cx="515" cy="181" r="136" fill="#fff"/>
    <circle cx="515" cy="181" r="132" fill="var(--brand-red)"/>
    <defs>
      <radialGradient id="portraitTone" cx="50%" cy="45%" r="60%">
        <stop offset="0" stop-color="#8a7468"/>
        <stop offset="1" stop-color="#b9bcb2"/>
      </radialGradient>
    </defs>
    <circle cx="515" cy="181" r="126" fill="url(#portraitTone)" role="img" aria-label="Portrait photo of Marvin Pold"/>
    <path class="band band--gray" d="M0,176 C180,160 330,196 420,248 C470,272 545,252 664,190 L664,322 C560,330 460,302 380,278 C280,252 150,250 0,272 Z" fill="var(--band-gray)"/>
    <path class="band band--red" d="M0,274 C150,252 280,254 380,280 C460,304 560,332 664,324 L664,430 L0,430 Z" fill="var(--brand-red)" stroke="#fff" stroke-width="2"/>
  </svg>

  <div class="wordmark">MPOLD REALTY</div>

  <div class="identity">
    <div class="identity__name">Marvin Pold</div>
    <div class="identity__role">Broker/Owner</div>
  </div>

  <ul class="contacts">
    <li><svg viewBox="0 0 16 16"><rect x="4" y="1" width="8" height="14" rx="1.5" fill="#fff"/><circle cx="8" cy="12.5" r="1" fill="var(--brand-red)"/><rect x="5.5" y="3" width="5" height="6" fill="var(--brand-red)"/></svg>555.210.3367</li>
    <li><svg viewBox="0 0 16 16"><rect x="1" y="3.5" width="14" height="9" fill="none" stroke="#fff" stroke-width="1.3"/><path d="M1 3.5 L8 9 L15 3.5 M1 12.5 L6 7.5 M15 12.5 L10 7.5" fill="none" stroke="#fff" stroke-width="1.3"/></svg>Marvin@MPoldRealty.com</li>
    <li><svg viewBox="0 0 16 16"><g fill="none" stroke="#fff" stroke-width="1.2"><circle cx="8" cy="8" r="6.5"/><ellipse cx="8" cy="8" rx="3" ry="6.5"/><path d="M1.5 8 H14.5"/></g></svg>www.MPoldRealty.com</li>
  </ul>
</section>

<section class="card card--back">
  <div class="wordmark">MPOLD REALTY</div>
  <div class="social"><span class="social__marker"></span>the_pinecrest_realtor</div>
</section>

</body>
</html>
```